Business card Zottelgarten

Business card is for a self-employed dog trainer with own dog school. Name and logo of the dog school are available. Color specifications as well. The design should be classy and minimalist, but also modern. An already existing idea would be: Front: Only the logo Back: Contact data

Font styles to use
Serif
Sans Serif
Other font styles liked:
• Trajan Pro

Colors
f78f20

Requirements
Must have
• Name: Margit Wendler-Rasch Title: Dipl. Dog Trainer Contain my logo Follow my font and color preferences (see files)

```html
<!DOCTYPE html>
<html lang="en">
<head>
<meta charset="utf-8">
<title>Zottelgarten – Business Card</title>
<link rel="stylesheet" href="https://fonts.googleapis.com/css2?family=Cinzel:wght@400&family=Source+Sans+3:wght@400;700&display=swap">
<style>
  :root {
    --page-bg: #e9e6e2;
    --card-top: #efedeb;
    --card-bottom: #d9d6d3;
    --card-edge: #c9c5c1;
    --emblem: #3d332e;
    --emblem-ring: #f2f0ee;
    --ink: #3a312c;
    --ink-soft: #6e6661;
  }
  html, body {
    margin: 0;
    width: 1200px;
    height: 969px;
    overflow: hidden;
    background: var(--page-bg);
  }
  .card {
    position: absolute;
    left: 100px;
    top: 200px;
    width: 1000px;
    height: 570px;
    border-radius: 24px;
    background: linear-gradient(160deg, var(--card-top), var(--card-bottom));
    box-shadow: 0 0 0 1px var(--card-edge), 0 18px 40px rgba(60, 50, 40, 0.15);
    overflow: hidden;
    font-family: "Source Sans 3", "Myriad Pro", sans-serif;
    color: var(--ink);
  }
  .emblem {
    position: absolute;
    left: 8px;
    top: 0;
    width: 570px;
    height: 570px;
  }
  .notch {
    position: absolute;
    right: -16px;
    top: 64px;
    width: 34px;
    height: 40px;
    border-radius: 50%;
    background: var(--emblem);
  }
  .holder {
    position: absolute;
    right: 35px;
    top: 50px;
    text-align: right;
  }
  .holder-name {
    margin: 0;
    font-weight: 700;
    font-size: 31px;
    letter-spacing: 0.5px;
    line-height: 1;
  }
  .holder-title {
    margin: 8px 0 0;
    font-size: 23px;
    color: var(--ink-soft);
    line-height: 1;
  }
  .address {
    position: absolute;
    right: 35px;
    top: 208px;
    margin: 0;
    text-align: right;
    font-style: normal;
    font-size: 22px;
    line-height: 30px;
  }
  .contacts {
    position: absolute;
    right: 28px;
    top: 285px;
    margin: 0;
    padding: 0;
    list-style: none;
    font-size: 22px;
    line-height: 31.5px;
  }
  .contacts li {
    display: flex;
    justify-content: flex-end;
    align-items: center;
    gap: 14px;
  }
  .contacts svg {
    width: 20px;
    height: 20px;
    fill: var(--ink);
  }
  .brand {
    position: absolute;
    right: 30px;
    top: 456px;
    text-align: right;
  }
  .brand-name {
    margin: 0;
    font-family: "Cinzel", "Trajan Pro", serif;
    font-size: 48px;
    line-height: 1;
    letter-spacing: 2px;
    color: var(--ink);
  }
  .brand-url {
    margin: 6px 0 0;
    font-family: "Cinzel", "Trajan Pro", serif;
    font-size: 15px;
    letter-spacing: 6px;
    color: var(--ink);
  }
</style>
</head>
<body>
  <main class="card">
    <svg class="emblem" viewBox="0 0 570 570" role="img" aria-label="Dog school emblem: silhouettes of a large and a small dog inside a round dark badge">
      <circle cx="285" cy="285" r="284" fill="var(--emblem)"/>
      <circle cx="285" cy="285" r="262" fill="none" stroke="var(--emblem-ring)" stroke-width="3" opacity="0.8"/>
    </svg>
    <span class="notch"></span>

    <header class="holder">
      <h1 class="holder-name">MARGIT WENDLER-RASCH</h1>
      <p class="holder-title">DIPL. DOG TRAINER</p>
    </header>

    <address class="address">2170 Birchwood Lane<br>Elm Ridge, NY 11920</address>

    <ul class="contacts">
      <li>555 0142 7781
        <svg viewBox="0 0 20 20" aria-hidden="true"><path d="M2 7c0-3 3-4 8-4s8 1 8 4v1h-4V6.5c-1-.5-2.5-.7-4-.7s-3 .2-4 .7V8H2zM5 10l2-3h6l2 3v6H5zm5 1.5a2 2 0 100 4 2 2 0 000-4z"/></svg>
      </li>
      <li>555 0193 4406
        <svg viewBox="0 0 20 20" aria-hidden="true"><path d="M6 1h8a1.5 1.5 0 011.5 1.5v15A1.5 1.5 0 0114 19H6a1.5 1.5 0 01-1.5-1.5v-15A1.5 1.5 0 016 1zm.5 2.5v11h7v-11zM10 15.5a1 1 0 100 2 1 1 0 000-2z"/></svg>
      </li>
      <li>555 0178 2259
        <svg viewBox="0 0 20 20" aria-hidden="true"><path d="M5 2h10v5H5zM2 8h16v7h-3v3H5v-3H2zm5 5v3h6v-3z"/></svg>
      </li>
      <li>margit@zottelgarten.ch
        <svg viewBox="0 0 20 20" aria-hidden="true"><path d="M2 4h16v1.5l-8 5-8-5zm0 3.5l8 5 8-5V16H2z"/></svg>
      </li>
      <li>www.zottelgarten.ch
        <svg viewBox="0 0 20 20" aria-hidden="true"><path d="M10 1.5a8.5 8.5 0 110 17 8.5 8.5 0 010-17zm-1 4L6.5 9l2 1.5-1 3 2 2 .5-3 2.5-1.5-1-3 2-1.5A6 6 0 009 5.5z"/></svg>
      </li>
    </ul>

    <footer class="brand">
      <p class="brand-name">ZOTTELGARTEN</p>
      <p class="brand-url">WWW.ZOTTELGARTEN.CH</p>
    </footer>
  </main>
</body>
</html>
```